Formal letterhead for Commercial Real Estate Company

Formal and professional letterhead for the transactional documents of a commercial real estate company.

Elements to be Included between header and footer:

- Logo (attached)(should be applied without the yellow background, in other words, the background colour for the design should be white)
- Slogan: Your Property Solution
- Physical Address: 27 Kestrel Lane, Ferndale, Durban, 4001
- Postal Address: PO Box 61894, Windermere, 4062
- Phone: 031 486 9142
- Fax: 031 337 8129
- Website: www.terrabuild.co.zaz
- eMail: contact@terrabuild.co.za

The brand guide is attached (the one you last provided), it does not provide direction on letterhead specifically but on other brand aspects.

Industry/Entity Type

Real Estate

```html
<!DOCTYPE html>
<html lang="en">
<head>
<meta charset="utf-8">
<title>TerraBuild Letterhead</title>
<link href="https://fonts.googleapis.com/css2?family=Open+Sans:ital,wght@0,400;0,700;1,400&display=swap" rel="stylesheet">
<style>
  :root {
    --backdrop: #e6e6e6;
    --paper: #ffffff;
    --ink: #111111;
    --ink-soft: #1a1a1a;
    --ghost: #f5f5f5;
    --rule: #1e1e1e;
  }
  * { margin: 0; padding: 0; box-sizing: border-box; }
  html, body {
    width: 1200px; height: 1200px; overflow: hidden;
    background: var(--backdrop);
    font-family: "Open Sans", sans-serif;
  }
  .letterhead {
    position: absolute; left: 197px; top: 30px;
    width: 806px; height: 1140px;
    background: var(--paper);
    overflow: hidden;
  }
  .brand {
    position: absolute; left: 32px; top: 34px;
  }
  .brand-name {
    display: flex; align-items: center; gap: 8px;
    font-weight: 700; font-size: 27px; letter-spacing: 0.5px;
    color: var(--ink); line-height: 1;
  }
  .brand-square {
    width: 22px; height: 22px; background: var(--ink);
  }
  .slogan {
    position: absolute; left: 34px; top: 123px;
    font-style: italic; font-size: 18px; color: var(--ink);
  }
  .contact {
    position: absolute; left: 567px; top: 38px;
    font-size: 13px; line-height: 16.5px; color: var(--ink-soft);
    font-style: normal;
  }
  .ghost-name {
    position: absolute; left: 70px; top: 760px;
    font-weight: 700; font-size: 200px; line-height: 1;
    letter-spacing: -4px; color: var(--ghost);
    white-space: nowrap;
  }
  .ghost-block {
    position: absolute; left: 78px; top: 1020px;
    width: 690px; height: 130px; background: var(--ghost);
  }
  .footer-rule {
    position: absolute; left: 0; bottom: 0;
    width: 530px; height: 9px; background: var(--rule);
  }
  .house-art {
    position: absolute; left: 506px; top: 1025px;
    width: 224px; height: 115px;
    background: linear-gradient(180deg, #1a1a1a, #000000);
  }
</style>
</head>
<body>
  <main class="letterhead">
    <header>
      <div class="brand">
        <div class="brand-name"><span class="brand-square"></span>TERRABUILD</div>
      </div>
      <p class="slogan">Your Property Solution</p>
      <address class="contact">
        PO Box 61894, Windermere, 4062<br>
        Phone: 031 486 9142<br>
        Fax: 031 337 8129<br>
        www.terrabuild.co.zaz<br>
        contact@terrabuild.co.za
      </address>
    </header>
    <footer>
      <div class="ghost-name" aria-hidden="true">TERRA</div>
      <div class="ghost-block" aria-hidden="true"></div>
      <div class="footer-rule"></div>
      <div class="house-art" role="img" aria-label="Black silhouette of a house with pitched roofs and a porch"></div>
    </footer>
  </main>
</body>
</html>
```